WinterCommuters

First, let me apologize for the short term. We just got an opportunity to place an ad in a commuter newspaper that will run throughout the winter months. We have tropical vacation rentals in Mexico, so it seems worth a shot.

We want to emphasize tropical luxury at competitive prices. Because we will be new to the audience, we need to cover a lot in one ad - images can definitely help. We are supplying photographs - feel free to crop or whatever.

We have the only private complex of luxury houses on the Mexican Caribbean coast, the "Riviera Maya" so we can accommodate anywhere from a single couple to a full wedding party. We want to show our large capacity without scaring off the single couple or small family with mom, dad, and a couple of kids.
Updates

Correction to text:  third paragraph.  The word should be "you", not "so" after "Riviera Maya,"
"As we are in the heart of the Riviera Maya, you will have "

Target Market(s)

Professionals looking to get out of the winter cold. Think tropical!

Industry/Entity Type

Wedding

Requirements
Must have
• The ad must be 5"x5" at 200 DPI (1,000 x 1000 pixels).
• The primary ad will be printed in black and white so it should be saved as a grayscale image. (I think they actually want a jpg, although a tiff would seem more logical!)
• The add will also be on the web in full color so please design the ad with color in mind and then change to grayscale after the content ends.
• Include our logo, phone number, e-mail, and website.
• Also, unless there is a good reason not to, include the four "first tier" images.
• Use the text as provided - not that some is optional.
Nice to have
• Please see the text in the attachments. OOPS: I downloaded the wrong version first - use the most recent "chicagoad" text!
• Also, unless there is a strong reason, use the "first tier" photos. We want to emphasize the accommodations, but also show large groups. We don't want to scare off the smaller groups (couples, small families) with the impression that we are only for large groups.
• The "second tier" photos are available if they would help. Both accommodation and weddings/large groups.
Should not have
• Stock photographs.
• I have (obviously) had some issues loading my files so please forgive the duplicates.

```html
<!DOCTYPE html>
<html lang="en">
<head>
<meta charset="utf-8">
<title>Tropical Villas Ad</title>
<link rel="stylesheet" href="https://fonts.googleapis.com/css2?family=Arimo:wght@400;700&family=Yellowtail&display=swap">
<style>
  :root {
    --stage: #1b1b1b;
    --band: #0e0e0d;
    --gold: #ecca5c;
    --green-top: #c6da58;
    --green-mid: #dfe99a;
    --green-low: #a9c944;
    --red: #c22a17;
    --orange: #f0a21c;
    --yellow: #f7d54a;
    --white: #ffffff;
    --frame: #e8f0b4;
    --body-font: "Arimo", Arial, sans-serif;
    --script-font: "Yellowtail", cursive;
  }
  html, body {
    margin: 0;
    padding: 0;
    width: 1200px;
    height: 900px;
    overflow: hidden;
    background: var(--stage);
  }
  .ad {
    position: absolute;
    left: 170px;
    top: 20px;
    width: 860px;
    height: 860px;
    overflow: hidden;
    background: linear-gradient(160deg, var(--green-top) 0%, var(--green-mid) 40%, var(--green-low) 100%);
    font-family: var(--body-font);
  }
  .ad-backdrop { position: absolute; inset: 0; }
  .header-band {
    position: absolute;
    left: 0; top: 0;
    width: 860px; height: 122px;
    background: var(--band);
  }
  .headline {
    position: absolute;
    left: 130px; top: 34px;
    margin: 0;
    font-family: var(--script-font);
    font-weight: 400;
    color: var(--gold);
    font-size: 36px;
    line-height: 36px;
    letter-spacing: 0.5px;
  }
  .headline span { display: block; }
  .flower-corner {
    position: absolute;
    left: 0; top: 0;
    width: 115px; height: 140px;
    background: radial-gradient(circle at 35% 40%, #8fd3e8 0%, #4fb0cf 35%, #9ccc3a 65%, rgba(156,204,58,0) 80%);
  }
  .flower-bottom {
    position: absolute;
    left: 620px; top: 660px;
    width: 240px; height: 200px;
    background: radial-gradient(circle at 60% 55%, #7fd0ea 0%, #3fa6cc 30%, #a6cf3c 55%, rgba(166,207,60,0) 75%);
  }
  .intro {
    position: absolute;
    left: 52px; top: 152px;
    width: 760px;
    margin: 0;
    color: var(--red);
    font-size: 17.5px;
    line-height: 19px;
  }
  .details {
    position: absolute;
    left: 52px; top: 222px;
    width: 760px;
    color: var(--red);
    font-size: 10.5px;
    line-height: 12px;
  }
  .details p { margin: 0 0 11px; }
  .promise {
    position: absolute;
    left: 52px; top: 346px;
    margin: 0;
    color: var(--white);
    font-size: 16px;
  }
  .invite {
    position: absolute;
    left: 52px; top: 372px;
    margin: 0;
    color: var(--red);
    font-size: 10.5px;
  }
  .photo {
    position: absolute;
    border: 3px solid var(--frame);
    box-sizing: border-box;
  }
  .photo-villa    { left: 53px;  top: 387px; width: 243px; height: 158px; background: linear-gradient(180deg, #9cc0e0, #c49a6a 55%, #6f7f45); }
  .photo-wedding  { left: 306px; top: 387px; width: 243px; height: 158px; background: linear-gradient(180deg, #7f9a5c, #d8d4c8 55%, #4f7a2a); }
  .photo-pool     { left: 558px; top: 387px; width: 244px; height: 158px; background: linear-gradient(180deg, #7fb2e6, #e3e9ef 45%, #2f86b8 75%, #b9a489); }
  .photo-bedroom  { left: 53px;  top: 554px; width: 182px; height: 86px;  background: linear-gradient(180deg, #d9c9b0, #f1ede6 60%, #b69a78); }
  .photo-townhouse{ left: 244px; top: 554px; width: 178px; height: 86px;  background: linear-gradient(180deg, #a9bfd4, #c9b28e 50%, #5e7a3c); }
  .photo-terrace  { left: 431px; top: 554px; width: 181px; height: 86px;  background: linear-gradient(180deg, #8fae6a, #6f5a3e 60%, #a8a070); }
  .photo-lounge   { left: 621px; top: 554px; width: 181px; height: 86px;  background: linear-gradient(180deg, #e4dccd, #8a6a4a 60%, #cbbfa9); }
  .facts {
    position: absolute;
    left: 52px; top: 656px;
    margin: 0;
    color: var(--red);
    font-size: 13px;
    line-height: 15px;
  }
  .brand {
    position: absolute;
    left: 52px; top: 703px;
    display: flex;
    align-items: center;
    gap: 8px;
    width: 150px;
  }
  .brand-dot {
    width: 22px; height: 22px;
    border-radius: 50%;
    background: var(--white);
    flex: none;
  }
  .brand-name {
    color: var(--white);
    font-size: 14px;
    line-height: 16px;
    font-weight: 400;
  }
  .contact {
    position: absolute;
    left: 200px; top: 700px;
    margin: 0;
    color: var(--white);
    font-size: 16px;
    line-height: 19px;
    font-style: normal;
  }
  .footer-band {
    position: absolute;
    left: 0; top: 836px;
    width: 860px; height: 24px;
    background: var(--band);
  }
</style>
</head>
<body>
  <section class="ad">
    <svg class="ad-backdrop" width="860" height="860" viewBox="0 0 860 860" aria-hidden="true">
      <path d="M300 140 C 520 120, 720 112, 860 100 L 860 140 C 700 138, 500 138, 300 140 Z" fill="#e2541c" opacity="0.85"/>
      <path d="M420 150 C 600 140, 760 138, 860 132 L 860 165 C 720 160, 560 156, 420 150 Z" fill="var(--orange)" opacity="0.9"/>
      <path d="M600 168 C 700 160, 800 158, 860 160 L 860 220 C 780 190, 700 175, 600 168 Z" fill="var(--yellow)" opacity="0.6"/>
      <path d="M0 790 C 220 760, 480 770, 860 730 L 860 780 C 520 800, 240 790, 0 812 Z" fill="var(--orange)"/>
      <path d="M0 805 C 260 790, 520 800, 860 770 L 860 795 C 540 815, 260 815, 0 826 Z" fill="#b3160e"/>
      <path d="M0 822 C 280 808, 560 818, 860 800 L 860 836 L 0 836 Z" fill="var(--yellow)"/>
    </svg>

    <div class="header-band"></div>
    <div class="flower-corner" role="img" aria-label="Decorative tropical flowers in blue and green"></div>
    <h1 class="headline">
      <span>Vacations, Weddings, Reunions, Retreats</span>
      <span>Wouldn’t you rather be in a tropical paradise?</span>
    </h1>

    <p class="intro">Come and relax in the only private complex of luxury houses on the beautiful Mexican Riviera. Only 60 miles South of Cancun, we are a world apart from the noise and crowds of large hotels and party towns.</p>

    <div class="details">
      <p>Located in the quiet coastal village of Akumal, you get all of the best amenities, great restaurants,<br>magnificent snorkeling and diving, beaches, and more in the laid back atmosphere that is so hard to find.<br>As we are in the heart of the Riviera Maya, you will have access to shopping,<br>Mayan ruins, tourist attractions, golf, sailing, diving and much more.</p>
      <p>Are you a couple looking for that perfect, secluded getaway?<br>Are you looking for a vacation in a quiet, safe, family-friendly area?<br>Do you have a family reunion, wedding, or retreat and you want everyone to be together?</p>
    </div>

    <p class="promise">With 5 luxury homes to choose from, we can meet your exact needs.</p>
    <p class="invite">Visit our web site or call us directly.  We look forward to hearing from you and to sharing our homes with you, your family and friends.</p>

    <div class="photo photo-villa" role="img" aria-label="Photo of the villa courtyard with palms and fountain"></div>
    <div class="photo photo-wedding" role="img" aria-label="Photo of an outdoor wedding ceremony with guests"></div>
    <div class="photo photo-pool" role="img" aria-label="Photo of the infinity pool overlooking the lagoon"></div>
    <div class="photo photo-bedroom" role="img" aria-label="Photo of a bright bedroom"></div>
    <div class="photo photo-townhouse" role="img" aria-label="Photo of the townhouses among the gardens"></div>
    <div class="photo photo-terrace" role="img" aria-label="Photo of a garden terrace with table and chairs"></div>
    <div class="photo photo-lounge" role="img" aria-label="Photo of a furnished living room"></div>

    <p class="facts">12 bedrooms, 15 beds, 17 bathrooms, and 5 pools.<br>Luxury Villas and Townhouses on Yal-Ku Lagoon, Akumal, Mexico</p>

    <div class="brand">
      <span class="brand-dot"></span>
      <span class="brand-name">Casa Laguna Villas</span>
    </div>
    <address class="contact">Daniel &amp; Nora Pryce<br>(555) 014-2290  ::  info@CasaLagunaVillas.com</address>

    <div class="flower-bottom" role="img" aria-label="Decorative tropical flowers in blue and lime green"></div>
    <div class="footer-band"></div>
  </section>
</body>
</html>
```